Plume - Stationary Design/Layout

We are a well established clothing design and manufacturing company (Plume Sourcing) based in London UK, with our own factory in Bangladesh, supplying to many fashion retailers and brands. Our factory has very high environmental and ethical standards with people at its heart. Our quality of garments are second to none.
Our new logo has been proudly developed by the Pixel Guild community last month, we are now in the second phase and need the layout designed for our letterheads, double sided business cards, compliment slip and clothing ticket. Feel as creative as you like, but make sure it looks great!!
***The Logo - the logo design and colour is set and should NOT be changed and stay on a dark grey backround. The logo artwork to use is attached.
***Details to use for the business card:
Dorian Hartley
Direct Line: 020 7946 0518
dorian@plumesourcing-mail.test
Plume Sourching Ltd.
58 - 60 Fenwick Row
Wrenholt . Oakvale
NW3 5QJ
Switchboard: 020 7946 0733
Fax: 020 7946 0733
www.plumesourcing-mail.test
***Details to use for the letterhead and compliment slip:
Plume Sourching Ltd.
58 - 60 Fenwick Row
Wrenholt . Oakvale
NW3 5QJ
Fax: 020 7946 0733
www.plumesourcing-mail.test
***Details for Swing Ticket:
Size: 12cm height by 5.5cm width
One side need to have just the logo without the 'Sourcing', on the other it needs to stay blank

```html
<!DOCTYPE html>
<html lang="en">
<head>
<meta charset="utf-8">
<title>Plume Sourcing – Stationery</title>
<link rel="stylesheet" href="https://fonts.googleapis.com/css2?family=Open+Sans:wght@400;600;700&display=swap">
<style>
  :root {
    --backdrop: #e6e4e1;
    --paper: #ffffff;
    --band-dark: #1f1f20;
    --band-mid: #3a3a3c;
    --band-light: #59595b;
    --band-edge: #2a2a2b;
    --logo-blue: #a8dde2;
    --ink: #2b2b2b;
    --ink-light: #ffffff;
    --rule: #9a9a9a;
  }
  * { box-sizing: border-box; margin: 0; padding: 0; }
  html, body {
    width: 1200px; height: 900px; overflow: hidden;
    background: var(--backdrop);
    font-family: "Open Sans", Arial, sans-serif;
  }
  .canvas { position: relative; width: 1200px; height: 900px; }

  .sheet {
    position: absolute; background: var(--paper);
    box-shadow: 0 1px 4px rgba(0,0,0,.18);
  }
  .band {
    position: absolute; left: 0; right: 0;
    background: linear-gradient(90deg, var(--band-dark) 0%, var(--band-mid) 55%, var(--band-light) 100%);
    border-top: 4px solid var(--band-edge);
    border-bottom: 4px solid var(--band-edge);
  }
  .wordmark {
    position: absolute; color: var(--logo-blue);
    font-weight: 600; white-space: nowrap; letter-spacing: .02em;
  }

  /* Letterhead */
  .letterhead { left: 15px; top: 58px; width: 556px; height: 785px; }
  .letterhead .band { top: 19px; height: 76px; }
  .letterhead .wordmark { left: 18px; top: 20px; font-size: 22px; }
  .contact {
    position: absolute; display: flex; color: var(--ink-light);
    font-size: 8.5px; line-height: 1.35; white-space: nowrap;
  }
  .contact .address { padding-right: 9px; }
  .contact .lines { padding-left: 9px; border-left: 1px solid var(--rule); }
  .contact strong { font-weight: 700; }
  .letterhead .contact { left: 290px; top: 18px; }
  .web {
    position: absolute; font-size: 11px; letter-spacing: .18em; color: var(--ink);
    white-space: nowrap;
  }
  .letterhead .web { right: 18px; bottom: 12px; }

  /* Business card front */
  .business-card {
    left: 656px; top: 89px; width: 235px; height: 135px;
    border-radius: 6px; overflow: hidden;
  }
  .business-card .band { top: 10px; height: 116px; border-width: 3px; }
  .business-card .wordmark { left: 13px; top: 45px; font-size: 15px; }
  .card-details {
    position: absolute; right: 12px; top: 10px; text-align: right;
    color: var(--ink-light); font-size: 5.5px; line-height: 1.35; white-space: nowrap;
  }
  .card-details .name { font-weight: 700; margin-bottom: 6px; }
  .card-details p + p { margin-top: 5px; }

  /* Compliment slip */
  .compliment-slip { left: 627px; top: 254px; width: 556px; height: 262px; }
  .compliment-slip .band { top: 17px; height: 68px; }
  .compliment-slip .wordmark { left: 18px; top: 16px; font-size: 22px; }
  .slip-title {
    position: absolute; right: 34px; top: 21px;
    color: var(--ink-light); font-size: 13px; letter-spacing: .2em;
  }
  .compliment-slip .contact { right: 34px; bottom: 14px; color: var(--ink); text-align: right; }

  /* Business card reverse */
  .card-reverse {
    left: 628px; top: 543px; width: 555px; height: 261px;
    background: var(--band-edge);
  }
  .card-reverse .panel {
    position: absolute; inset: 10px;
    background: linear-gradient(90deg, var(--band-light) 0%, var(--band-mid) 50%, var(--band-dark) 100%);
  }
  .card-reverse .wordmark { left: 0; right: 0; top: 92px; text-align: center; font-size: 36px; }
  .card-reverse .web { left: 0; right: 0; bottom: 14px; text-align: center; color: var(--ink-light); }
</style>
</head>
<body>
<main class="canvas">

  <section class="sheet letterhead" aria-label="Letterhead">
    <div class="band">
      <span class="wordmark">Plume Sourcing</span>
      <div class="contact">
        <div class="address">
          <strong>Plume Sourching Ltd.</strong><br>
          58 - 60 Fenwick Row<br>
          Wrenholt . Oakvale&nbsp; NW3 5QJ
        </div>
        <div class="lines">
          Switchboard: 020 7946 0733<br>
          Fax: 020 7946 0733
        </div>
      </div>
    </div>
    <p class="web">www.plumesourcing-mail.test</p>
  </section>

  <section class="sheet business-card" aria-label="Business card">
    <div class="band">
      <span class="wordmark">Plume Sourcing</span>
      <div class="card-details">
        <p class="name">Dorian Hartley</p>
        <p>Direct Line: 020 7946 0518<br>dorian@plumesourcing-mail.test</p>
        <p>Plume Sourching Ltd.<br>58 - 60 Fenwick Row<br>Wrenholt . Oakvale<br>NW3 5QJ</p>
        <p>Switchboard: 020 7946 0733<br>Fax: 020 7946 0733<br>www.plumesourcing-mail.test</p>
      </div>
    </div>
  </section>

  <section class="sheet compliment-slip" aria-label="Compliment slip">
    <div class="band">
      <span class="wordmark">Plume Sourcing</span>
      <span class="slip-title">WITH COMPLIMENTS</span>
    </div>
    <div class="contact">
      <div class="address">
        <strong>Plume Sourching Ltd.</strong><br>
        58 - 60 Fenwick Row<br>
        Wrenholt . Oakvale&nbsp; NW3 5QJ
      </div>
      <div class="lines">
        Switchboard: 020 7946 0733<br>
        Fax: 020 7946 0733
      </div>
    </div>
  </section>

  <section class="sheet card-reverse" aria-label="Business card reverse">
    <div class="panel">
      <span class="wordmark">Plume Sourcing</span>
      <p class="web">www.plumesourcing-mail.test</p>
    </div>
  </section>

</main>
</body>
</html>
```